Malvora Vitamins

I am reaching out to discuss a design project for a food supplement line for my company, Malvora Pharma GmBH. I am looking for a design that is colorful, creative, consistent, and indicative of each product. Initially, we have two items in our product range:
1. Folic Acid 400 with B12+B6 (Box)
2. Vitamin D3 50,000 IU (Label)
I have attached the source files from another company for each item, including the die cuts, so feel free to change the logo and address and come up with a new theme.
The new address is: Kolbergweg 42 .36211 Fulda, Germany

Target Market(s)

Middle East

Industry/Entity Type

Vitamins

Font styles to use
Sans Serif

Colors
0054AA
0677BA
7BADD7
CADEEF
E8F1F8
6B429C
8869AF
B7A5CE
E3DAEB
F3F0F8

Requirements
Must have
• Flores and photos to iditify the product

```html
<!DOCTYPE html>
<html lang="en">
<head>
<meta charset="utf-8">
<title>Malvora Vitamins – Folic Acid Box &amp; Vitamin D3 Label</title>
<link href="https://fonts.googleapis.com/css2?family=Poppins:wght@400;500;600;700;800&family=Roboto+Condensed:wght@400;500;700&display=swap" rel="stylesheet">
<style>
  :root{
    --stage:#e6e6e6;
    --navy:#1553a6;
    --blue-text:#1d4fa0;
    --white:#ffffff;
    --teal-top:#86bf78;
    --teal-mid:#6fb59a;
    --teal-bottom:#4ea6c6;
    --row-line:rgba(255,255,255,.55);
    --label-yellow:#e9c96e;
    --label-orange:#f29a3b;
    --label-deep:#ee7a2b;
    --die-line:#3a5bb8;
  }
  *{box-sizing:border-box;margin:0;padding:0}
  html,body{width:1200px;height:1000px;overflow:hidden;background:var(--stage)}
  body{font-family:"Poppins",sans-serif;color:var(--white);position:relative}
  .stage{position:relative;width:1200px;height:1000px}

  /* ---------- Folic acid carton ---------- */
  .carton{position:absolute;left:224px;top:108px;width:751px;height:447px;overflow:hidden}
  .carton-top{position:absolute;left:0;top:0;width:751px;height:58px;background:var(--white)}
  .carton-stripe{position:absolute;left:0;top:58px;width:751px;height:6px;background:var(--navy)}
  .carton-body{position:absolute;left:0;top:64px;width:751px;height:383px;
    background:
      radial-gradient(ellipse 190px 150px at 233px 0px, rgba(150,200,95,.9), rgba(150,200,95,0) 100%),
      linear-gradient(180deg,var(--teal-top) 0%,var(--teal-mid) 45%,var(--teal-bottom) 100%)}
  .fold{position:absolute;top:0;width:1px;height:447px;background:rgba(40,80,170,.55)}
  .carton-bottom{position:absolute;left:0;top:0}

  .brand{font-family:"Poppins",sans-serif;font-weight:600;color:var(--navy);letter-spacing:.22em;white-space:nowrap}
  .brand-top{position:absolute;top:14px;font-size:19px;transform:translateX(-50%)}
  .brand-spine{position:absolute;font-size:14px;color:var(--white);transform:translate(-50%,-50%) rotate(90deg);letter-spacing:.2em}

  .product-title{position:absolute;left:233px;top:98px;transform:translateX(-50%);text-align:center;font-weight:800;font-size:56px;line-height:52px;letter-spacing:.04em}
  .strength{position:absolute;left:233px;top:216px;transform:translateX(-50%);font-size:14px;font-weight:400;letter-spacing:.05em}
  .ribbon-line{position:absolute;height:1px;background:var(--white)}
  .ribbon{position:absolute;background:var(--white);color:var(--blue-text);
    font-family:"Roboto Condensed",sans-serif;font-weight:500;display:flex;align-items:center;justify-content:center;
    clip-path:polygon(0 0,100% 0,96% 50%,100% 100%,0 100%,4% 50%)}
  .carton-ribbon{left:156px;top:244px;width:157px;height:20px;font-size:13px}
  .claims{position:absolute;left:109px;top:303px;font-size:9.5px;line-height:11px;font-weight:400}
  .claims p{margin-bottom:9.5px}

  .molecule-art{position:absolute;border-radius:50%;
    background:radial-gradient(ellipse at center,rgba(30,170,180,.55) 0%,rgba(30,170,180,.25) 55%,rgba(30,170,180,0) 75%)}

  .made-in{position:absolute;left:150px;top:414px;font-weight:700;font-size:11.5px;line-height:10.5px}
  .flag{position:absolute;left:109px;top:407px;width:31px;height:31px;border-radius:50%;overflow:hidden;
    background:linear-gradient(180deg,#111 0 33.3%,#dd1c1c 33.3% 66.6%,#f6c400 66.6% 100%)}
  .count-tag{position:absolute;background:var(--white);color:var(--blue-text);text-align:center;border-radius:3px 3px 0 0}
  .carton-count{left:301px;top:399px;width:45px;height:48px;padding-top:5px}
  .count-tag .num{display:block;font-weight:700;font-size:22px;line-height:22px}
  .count-tag .unit{display:block;font-size:6.5px;letter-spacing:.05em;line-height:8px}

  /* back panel */
  .table{position:absolute;font-family:"Roboto Condensed",sans-serif;font-size:5.6px}
  .table-head{background:var(--navy);color:var(--white);font-family:"Poppins",sans-serif;font-weight:600;font-size:6.5px;text-align:center;height:13px;line-height:13px;border-radius:2px 2px 0 0}
  .table-cols{background:var(--white);color:#222;display:grid;height:12px;align-items:center;padding:0 4px}
  .table-row{display:grid;height:12px;align-items:center;border-bottom:1px solid var(--row-line);padding:0 4px;color:var(--white)}
  .nutrition{left:485px;top:82px;width:119px}
  .nutrition .table-cols,.nutrition .table-row{grid-template-columns:44px 30px 37px}
  .composition{left:485px;top:209px;width:119px}
  .composition .table-cols,.composition .table-row{grid-template-columns:44px 30px 37px}
  .r{text-align:right}
  .c{text-align:center}
  .nrv-note{position:absolute;left:488px;top:280px;width:118px;font-size:5px;line-height:6px}
  .maker{position:absolute;left:485px;top:367px;font-size:7px;line-height:8.5px}
  .net{position:absolute;left:485px;top:400px;font-size:7px}
  .back-copy{position:absolute;left:618px;top:82px;width:117px;font-size:7px;line-height:8.4px;text-align:justify}
  .back-copy h4{font-weight:600;font-size:7px;margin-top:7px}
  .back-copy ul{list-style:none}
  .back-copy li{padding-left:6px;text-indent:-6px;text-align:left}
  .back-copy li::before{content:"• "}

  .flap{position:absolute;left:975px;top:108px}

  /* ---------- Vitamin D3 label ---------- */
  .label{position:absolute;left:321px;top:649px;width:557px;height:242px;border-radius:9px;overflow:hidden;
    background:
      radial-gradient(ellipse 260px 200px at 0 0,var(--label-yellow),rgba(233,201,110,0) 100%),
      linear-gradient(100deg,#eebc5c 0%,var(--label-orange) 45%,var(--label-deep) 100%)}
  .label-copy{position:absolute;left:19px;top:18px;width:150px;font-size:7px;line-height:8.4px}
  .label-copy h4{font-weight:600;font-size:7px;margin-top:7px}
  .label-copy h4:first-child{margin-top:0}
  .label-copy ul{list-style:none}
  .label-copy li{padding-left:5px;text-indent:-5px}
  .label-copy li::before{content:"• "}
  .label-brand{left:279px;top:20px;font-size:18px;transform:translateX(-50%)}
  .label-title{position:absolute;left:279px;top:62px;transform:translateX(-50%);text-align:center;font-weight:800;font-size:36px;line-height:30px;letter-spacing:.05em}
  .label-ribbon{left:230px;top:129px;width:96px;height:16px;font-size:12px}
  .label-claim{position:absolute;left:279px;top:160px;transform:translateX(-50%);text-align:center;font-size:10.5px;line-height:11.5px;letter-spacing:.03em;white-space:nowrap}
  .batch{position:absolute;left:12px;top:214px;font-size:5.8px;line-height:7.8px}
  .dietary{position:absolute;left:201px;top:216px;font-weight:700;font-size:8.5px;line-height:8.5px;letter-spacing:.03em}
  .label-count{left:314px;top:202px;width:42px;height:40px;padding-top:3px}
  .label-count .num{font-size:17px;line-height:18px}
  .label-count .unit{font-size:5.6px;line-height:5.5px}

  .facts{position:absolute;left:394px;top:12px;width:140px;font-family:"Roboto Condensed",sans-serif;font-size:5.3px;color:var(--white)}
  .facts .table-head{height:13px;line-height:13px}
  .facts-block{border-bottom:1px solid var(--white);padding:5px 4px 2px}
  .facts-row{display:flex;justify-content:space-between;border-bottom:1px solid rgba(255,255,255,.7);height:9px;align-items:center;padding:0 4px}
  .facts-row.in1{padding-left:7px}
  .facts-row.in2{padding-left:10px}
  .kv{display:flex;justify-content:space-between;line-height:7.5px}
  .dv{text-align:center;border-bottom:1px solid var(--white);height:11px;line-height:11px}
  .facts-notes{font-size:3.4px;line-height:4.6px;padding:6px 4px 0}
  .facts-box{margin:8px 2px 0;border:1px solid var(--white);font-size:3.4px;line-height:4.6px;text-align:center;padding:2px}
</style>
</head>
<body>
<div class="stage">

  <!-- Folic Acid carton, flat die-line -->
  <div class="carton">
    <div class="carton-top"></div>
    <div class="carton-stripe"></div>
    <div class="carton-body"></div>

    <div class="molecule-art" role="img" aria-label="Teal molecule structure illustration" style="left:221px;top:209px;width:250px;height:200px"></div>
    <div class="molecule-art" role="img" aria-label="Small teal molecule cluster" style="left:370px;top:232px;width:110px;height:80px"></div>

    <svg class="carton-bottom" width="751" height="447" viewBox="0 0 751 447" aria-hidden="true">
      <path d="M92 399 H220 C245 399 252 428 280 428 H751 V447 H0 V428 H92 Z" fill="var(--navy)"/>
    </svg>

    <div class="fold" style="left:92px"></div>
    <div class="fold" style="left:374px"></div>
    <div class="fold" style="left:469px"></div>

    <div class="brand brand-top" style="left:233px">MALVORA</div>
    <div class="brand brand-top" style="left:610px">MALVORA</div>
    <div class="brand brand-spine" style="left:43px;top:138px">MALVORA</div>
    <div class="brand brand-spine" style="left:421px;top:138px">MALVORA</div>

    <div class="product-title">FOLIC<br>ACID</div>
    <div class="strength">400 µG</div>
    <div class="ribbon-line" style="left:111px;top:254px;width:43px"></div>
    <div class="ribbon-line" style="left:314px;top:254px;width:43px"></div>
    <div class="ribbon carton-ribbon">WITH VITAMIN B12 &amp; B6</div>

    <div class="claims">
      <p>Made to High Standards<br>of Quality Control</p>
      <p>No Artificial Colours<br>or Preservatives</p>
      <p>Suitable for Vegans</p>
    </div>

    <div class="flag" role="img" aria-label="German flag"></div>
    <div class="made-in">MADE IN<br>GERMANY</div>
    <div class="count-tag carton-count"><span class="num">30</span><span class="unit">TABLETS</span></div>

    <!-- back panel -->
    <div class="table nutrition">
      <div class="table-head">Nutritional information</div>
      <div class="table-cols"><span>Nutritional Values</span><span class="c">Per Tablet</span><span class="c">Per 100 g</span></div>
      <div class="table-row"><span>Energy</span><span class="r">2 kJ / 0 kcal</span><span class="r">1406 kJ / 335 kcal</span></div>
      <div class="table-row"><span>Fat</span><span class="r">&lt; 0.1 g</span><span class="r">1.5 g</span></div>
      <div class="table-row"><span>of which saturates</span><span class="r">&lt; 0.1 g</span><span class="r">1.5 g</span></div>
      <div class="table-row"><span>Carbohydrate</span><span class="r">&lt; 0.1 g</span><span class="r">74.3 g</span></div>
      <div class="table-row"><span>of which sugars</span><span class="r">&lt; 0.1 g</span><span class="r">20.5 g</span></div>
      <div class="table-row"><span>Protein</span><span class="r">&lt; 0.1 g</span><span class="r">&lt; 0.1 g</span></div>
      <div class="table-row"><span>Salt</span><span class="r">&lt; 0.01 g</span><span class="r">0.05 g</span></div>
    </div>

    <div class="table composition">
      <div class="table-head">Composition</div>
      <div class="table-cols"><span class="c">Ingredients</span><span class="c">Per Tablet</span><span class="c">%NRV*</span></div>
      <div class="table-row"><span>Vitamin B6</span><span class="r">1.9 mg</span><span class="r">136</span></div>
      <div class="table-row"><span>Folic Acid</span><span class="r">600 µg</span><span class="r">300</span></div>
      <div class="table-row"><span>Vitamin B12</span><span class="r">2.6 µg</span><span class="r">104</span></div>
    </div>
    <p class="nrv-note">* NRV = Nutrient Reference Values according to Regulation (EU) Nr. 1169/2011</p>

    <p class="maker">Made in Germany By:<br>R. Vollmerhaus GmbH &amp; Co. KG.</p>
    <p class="net">Net weight 3.6 g</p>

    <div class="back-copy">
      <p>Folic Acid is a food supplement rich in folic acid and vitamins B6 &amp; B12. Folate, Vitamins B6 and B12 contribute to normal homocysteine metabolism and red blood cells formation.</p>
      <h4>Ingredients</h4>
      <p>Starch; Maltodextrin; Bulking Agents: Lactose Monohydrate (contains Milk), Microcrystalline Cellulose; Cyanocobalamin (Vitamin B12); Pyridoxine hydrochloride (Vitamin B6); Anti-Caking Agent: Magnesium Salts of Fatty Acids; Pteroylmonoglutamic Acid (Folic Acid).</p>
      <h4>Directions for use</h4>
      <p style="text-align:left">For adults, take one tablet daily with sufficient amount of water.</p>
      <h4>Precautions</h4>
      <ul>
        <li>Keep out of reach of children.</li>
        <li>The recommended daily intake indicated may not be exceeded.</li>
        <li>Do not use after the expiry date printed on the box.</li>
      </ul>
      <p style="margin-top:7px"><strong style="font-weight:600">Disclaimer:</strong> Food supplements are not a substitute for a varied, balanced diet and a healthy way of living.</p>
      <h4>Storage Conditions</h4>
      <ul>
        <li>Store in the original package, in a cool (&lt; 25°C) and dry place.</li>
        <li>Protect the product from light and moisture.</li>
      </ul>
    </div>
  </div>

  <svg class="flap" width="56" height="448" viewBox="0 0 56 448" aria-hidden="true">
    <path d="M0.5 0.5 L54.5 14 V432 L0.5 447" fill="none" stroke="var(--die-line)" stroke-width="1"/>
  </svg>

  <!-- Vitamin D3 bottle label -->
  <div class="label">
    <div class="molecule-art" role="img" aria-label="Soft orange molecule structure illustration" style="left:110px;top:35px;width:170px;height:170px;background:radial-gradient(ellipse at center,rgba(240,120,40,.5) 0%,rgba(240,120,40,.2) 55%,rgba(240,120,40,0) 75%)"></div>

    <svg style="position:absolute;left:0;top:0" width="557" height="242" viewBox="0 0 557 242" aria-hidden="true">
      <path d="M0 204 H276 C296 204 300 226 318 226 H378 C386 226 388 234 389 242 H0 Z" fill="var(--navy)"/>
    </svg>

    <div class="label-copy">
      <h4>Directions for use:</h4>
      <p>Take 1 capsule per day with plenty of water.</p>
      <h4>Storage Conditions:</h4>
      <ul>
        <li>Store in a cool and dry place (≤ 25 °C).</li>
        <li>Best before end: see base.</li>
      </ul>
      <h4>Warnings:</h4>
      <ul>
        <li>The recommended daily intake indicated should not be exceeded.</li>
        <li>Keep out of reach of children.</li>
        <li>Do not use after expiry date.</li>
      </ul>
    </div>

    <div class="brand label-brand" style="position:absolute">MALVORA</div>
    <div class="label-title">VITAMIN<br>D3</div>
    <div class="ribbon-line" style="left:206px;top:137px;width:22px"></div>
    <div class="ribbon-line" style="left:328px;top:137px;width:24px"></div>
    <div class="ribbon label-ribbon">50.000 IU</div>
    <div class="label-claim">SUPPORTS HEALTHY BONES<br>&amp; THE IMMUNE SYSTEM</div>

    <div class="batch">Batch No.:<br>Mfg. Date:<br>Exp. Date:</div>
    <div class="dietary">DIETARY<br>SUPPLEMENT</div>
    <div class="count-tag label-count"><span class="num">120</span><span class="unit">SOFTGEL<br>CAPSULE</span></div>

    <div class="facts">
      <div class="table-head">Supplement Facts</div>
      <div class="facts-block">
        <div class="kv"><span>Serving Per Container</span><span>120 Capsule</span></div>
        <div class="kv"><span>Serving Size</span><span>1 Capsule</span></div>
      </div>
      <div class="facts-block">
        <div class="kv"><span>Amount per serving</span><span></span></div>
        <div class="kv"><span>Calories</span><span>2</span></div>
      </div>
      <div class="dv">% Daily Value*</div>
      <div class="facts-row"><span>Total Fat 0g</span><span>0%</span></div>
      <div class="facts-row in1"><span>Saturated Fat 0g</span><span>0%</span></div>
      <div class="facts-row in1"><span>Trans Fat 0g</span><span>0%</span></div>
      <div class="facts-row"><span>Cholesterol 0mg</span><span>0%</span></div>
      <div class="facts-row"><span>Sodium 0g</span><span>0%</span></div>
      <div class="facts-row"><span>Total Carbohydrate 0g</span><span>0%</span></div>
      <div class="facts-row in1"><span>Dietary Fiber 0g</span><span>0%</span></div>
      <div class="facts-row in1"><span>Total Sugars 0g</span><span>0%</span></div>
      <div class="facts-row in2"><span>Includes 0g Added Sugars</span><span>0%</span></div>
      <div class="facts-row"><span>Protein 0g</span><span>0%</span></div>
      <div class="facts-row"><span>Vitamin D3 250µg</span><span>1250%</span></div>
      <div class="facts-notes">
        <p>**%DV not yet set.</p>
        <p>*The % Daily Value shows how much a nutrient in one serving adds to a daily diet of 2,000 calories.</p>
      </div>
      <div class="facts-box">†These statements have not been evaluated by the Food and Drug Administration. This product is not intended to diagnose, treat, cure, or prevent any disease.</div>
    </div>
  </div>

</div>
</body>
</html>
```